UK based media owner KELVANO (http://www.kelvano.uk/) needs DIGITAL ADVERT to run on our digital panel

Hi guys,

Thanks for taking the time to have a look at this brief.
I need someone to create a digital advert (still/static design or video) to run on our digital panels which are located across UK university student unions.
For who wants to upload a video ---> All of our panels are digitally enabled and allow for full motion video – they run adverts 10 seconds long (see artwork specification document in attachment) therefore the advert will have to be 10 seconds long.
For static/still design ----> see artwork specification to see resolution etc

I need something professional looking, polished yet fresh and exciting so that it speaks and connects to this younger audience – we want to inspire them to take a step towards new levels of business opportunities.

Here are some Key Points you’ll need to take into consideration when designing the advert:

Overall Campaign Objective: To excite and attract young entrepreneurs to get in touch with us for possible partnerships

Target Audience: Young entrepreneurs attending university (university students – 18 to 24 years old)

Creative Specifications: See attached document with artwork specifications

Text on Advert:

I need the following text to appear on the advert: (Please include company logo)

“Do you have a business idea that would benefit with advertising on these screens?

We want to support young entrepreneurs and will partner with any whom have a great idea

WE WANT TO HEAR FROM YOU!

Email us at ideas@kelvano.uk
www.kelvano.uk/ideas”

I would need some ideas by the 3rd July 2018 if possible.

Thanks to all who will take part in this project – contact me if you have any questions

Target Market(s)

Young entrepreneurs attending university (university students – 18 to 24 years old)

Requirements
Must have
• I need the following text to appear on the advert: (Please include company logo)
• “Do you have a business idea that would benefit with advertising on these screens?
• We want to support young entrepreneurs and will partner with any whom have a great idea
• WE WANT TO HEAR FROM YOU!
• Email us at ideas@kelvano.uk
• www.kelvano.uk/ideas”

```html
<!DOCTYPE html>
<html lang="en">
<head>
<meta charset="utf-8">
<title>KELVANO – Business Ideas</title>
<link href="https://fonts.googleapis.com/css2?family=Oswald:wght@200;700&family=Open+Sans:wght@400;700&display=swap" rel="stylesheet">
<style>
  :root {
    --red: #fe0a10;
    --ink: #231f20;
    --white: #ffffff;
    --grey: #bcbec0;
  }
  html, body { margin: 0; padding: 0; overflow: hidden; background: var(--ink); }
  .advert {
    position: relative;
    width: 675px;
    height: 1200px;
    overflow: hidden;
    background: var(--red);
    font-family: "Oswald", sans-serif;
  }
  .advert__shapes { position: absolute; inset: 0; width: 675px; height: 1200px; }
  .brand {
    position: absolute; left: 36px; top: 40px;
    margin: 0; color: var(--white);
    font: 700 50px/1 "Oswald", sans-serif;
    letter-spacing: 0.01em;
  }
  .headline { margin: 0; font-weight: normal; }
  .headline span {
    position: absolute; white-space: nowrap; line-height: 1;
  }
  .light { font-weight: 200; color: var(--ink); }
  .bold {
    font-weight: 700; color: var(--white);
    transform: scaleX(0.8); transform-origin: left top;
    letter-spacing: -0.01em;
  }
  .pitch {
    position: absolute; left: 389px; top: 812px; width: 270px;
    margin: 0; text-align: center; color: var(--white);
    font: 400 25.5px/29.6px "Open Sans", sans-serif;
  }
  .callout {
    position: absolute; left: 16px; top: 958px; width: 380px;
    margin: 0; text-align: center; color: var(--red);
    font: 700 56px/50px "Oswald", sans-serif;
    transform: scaleX(0.8); transform-origin: 190px 0;
    letter-spacing: -0.01em;
  }
  .contact {
    position: absolute; left: 430px; top: 1033px; width: 260px;
    margin: 0; text-align: center; color: var(--white);
    font: 400 25.5px/28px "Open Sans", sans-serif;
  }
  .footer-url {
    position: absolute; left: 0; top: 1112px; width: 675px; height: 88px;
    margin: 0; display: flex; align-items: center; justify-content: center;
    color: var(--white);
    font: 700 35px/1 "Open Sans", sans-serif;
  }
</style>
</head>
<body>
<main class="advert">
  <svg class="advert__shapes" viewBox="0 0 844 1500" aria-hidden="true">
    <path class="question-mark" fill="#000"
      d="M190,340 C215,170 340,50 500,50 C680,50 800,170 800,330 C800,470 700,540 620,610 C560,665 545,700 545,770 L445,770 C445,690 465,630 540,560 C640,470 695,420 695,320 C695,215 610,150 500,150 C390,150 310,230 280,358 Z"/>
    <circle class="question-dot" cx="496" cy="935" r="52" fill="#000"/>
    <polygon class="info-panel" points="440,1015 844,1015 844,1390 555,1390" fill="#231f20"/>
    <path class="wave-white" fill="#fff" d="M0,1390 L0,1205 C120,1075 300,1055 490,1180 L555,1390 Z"/>
    <path class="wave-grey" fill="none" stroke="#bcbec0" stroke-width="9"
      d="M0,1180 C120,1050 300,1030 490,1155 C620,1240 760,1255 844,1215"/>
    <path class="wave-black" fill="none" stroke="#000" stroke-width="10"
      d="M0,1195 C120,1066 300,1046 490,1171 C620,1256 760,1271 844,1231"/>
    <path class="wave-grey-low" fill="none" stroke="#bcbec0" stroke-width="7"
      d="M505,1210 C630,1275 760,1285 844,1250"/>
    <rect class="footer-band" x="0" y="1390" width="844" height="110" fill="#fe0a10"/>
  </svg>

  <p class="brand">KELVANO</p>

  <h1 class="headline">
    <span class="light" style="left:336px;top:137px;font-size:64px">Do you</span>
    <span class="light" style="left:334px;top:197px;font-size:64px">have a</span>
    <span class="bold" style="left:236px;top:255px;font-size:89px">business</span>
    <span class="bold" style="left:288px;top:340px;font-size:84px">idea</span>
    <span class="light" style="left:120px;top:419px;font-size:64px">that would</span>
    <span class="bold" style="left:84px;top:475px;font-size:89px">benefit</span>
    <span class="light" style="left:126px;top:563px;font-size:60px">with</span>
    <span class="bold" style="left:36px;top:600px;font-size:84px">advertising</span>
    <span class="light" style="left:110px;top:681px;font-size:64px">on these</span>
    <span class="bold" style="left:68px;top:718px;font-size:90px">screens</span>
  </h1>

  <p class="pitch">We want to support young entrepreneurs and will partner with any whom have a great idea</p>

  <p class="callout">WE WANT TO<br>HEAR FROM YOU!</p>

  <p class="contact">Email us at<br>ideas@kelvano.uk</p>

  <p class="footer-url">www.kelvano.uk/ideas</p>
</main>
</body>
</html>
```